Velkano Holdings Ltd - An invesmtent & trading company needs a web design

We need a web design for our company based in Cyprus. The company was founded in 2009. We have continuously grown and now invest & trade all over the world.

Velkano Holdings ltd. specializes in the buying and selling of crude oil, precious metals and the investment in properties.

We know that trust is of the utmost importance when it comes to business and the design should communicate this to prospective business partners. Find attached the company logo. The colour scheme for the website should use similar colours and ideally incorporate the logo in some shape or form as well.

Target Market(s)

Oil Traders, Metall Traders, Property Investments

Industry/Entity Type

Trade

Coding

Coded - Design and coding required

Number of Pages Required

4 page

Font styles to use
Sans Serif

Requirements
Must have
• Mainpage,
• About Us
• Partners
• Legal Notice

```html
<!DOCTYPE html>
<html lang="en">
<head>
<meta charset="utf-8">
<title>Velkano Holdings Ltd</title>
<link href="https://fonts.googleapis.com/css2?family=Open+Sans:wght@400;600;700&display=swap" rel="stylesheet">
<style>
:root{
  --navy:#17416e;
  --blue:#1f6db3;
  --sky:#2e8bd8;
  --yellow:#f6c400;
  --ink:#333d47;
  --muted:#7a828a;
  --light:#f2f3f4;
  --band:#e9eaeb;
  --footer:#232a31;
  --footer-deep:#1a1f25;
  --white:#ffffff;
}
*{box-sizing:border-box;margin:0;padding:0}
html,body{width:670px;height:1200px;overflow:hidden}
body{font-family:"Open Sans",Arial,sans-serif;color:var(--ink);background:var(--white);font-size:6px;line-height:1.5}
.page{width:670px;height:1200px;position:relative}

/* header */
.site-header{height:50px;display:flex;align-items:center;justify-content:space-between;padding:0 40px 0 150px;position:relative}
.brand{display:flex;align-items:center;gap:6px}
.brand-square{width:18px;height:18px;background:var(--blue)}
.brand-name{font-weight:700;font-size:13px;color:var(--navy);letter-spacing:.5px}
.top-links{position:absolute;right:40px;top:5px;font-size:5px;color:var(--muted);display:flex;gap:8px;align-items:center}
.top-links .flag{width:9px;height:6px;background:var(--blue);display:inline-block}
.main-nav{display:flex;margin-top:14px}
.main-nav a{font-size:5.5px;font-weight:700;color:var(--navy);text-decoration:none;padding:7px 7px;text-transform:uppercase}
.main-nav a.active{background:var(--blue);color:var(--white)}

/* hero */
.hero{height:147px;position:relative;display:flex}
.hero-photo{position:absolute;inset:0;background:linear-gradient(90deg,#6f8f4d 0%,#c9b27a 22%,#e7e3d6 45%,#f3f1ea 70%,#e9ecef 100%)}
.hero-copy{position:relative;margin-left:390px;margin-top:42px;width:210px}
.hero-title{font-size:12px;font-weight:700;color:var(--blue);line-height:1.2}
.hero-text{font-size:5.5px;color:var(--ink);margin:5px 0 8px}
.btn{display:inline-block;font-size:5.5px;font-weight:700;padding:5px 12px;border-radius:2px;text-decoration:none}
.btn-yellow{background:var(--yellow);color:var(--navy)}
.btn-blue{background:var(--blue);color:var(--white)}

/* about */
.about{display:flex;gap:30px;padding:30px 140px 0 140px;height:145px}
.about-copy{flex:1}
.about-title{font-size:11px;font-weight:700;color:var(--navy);margin-bottom:7px}
.about-copy p{font-size:5px;color:var(--muted);margin-bottom:6px}
.booking{width:140px;background:var(--blue);padding:10px 10px;color:var(--white);margin-top:-8px}
.booking h3{font-size:7px;font-weight:700;margin-bottom:6px}
.booking .field{height:11px;background:var(--white);margin-bottom:5px;font-size:4.5px;color:var(--muted);padding:2px 4px}
.booking .field.tall{height:20px}

/* save banner */
.save-banner{margin:8px 140px 0;height:44px;background:var(--yellow);display:flex;align-items:center;padding:0 14px;gap:10px}
.save-icon{width:28px;height:28px;border-radius:50%;background:var(--blue)}
.save-copy{flex:1}
.save-copy h3{font-size:11px;font-weight:700;color:var(--navy)}
.save-copy p{font-size:5px;color:var(--navy)}

/* section shared */
.section-title{text-align:center;font-size:11px;font-weight:600;color:var(--navy)}
.section-intro{text-align:center;font-size:5px;color:var(--muted);width:340px;margin:6px auto 0}
.dots{display:flex;justify-content:center;gap:4px;margin-top:8px}
.dots span{width:4px;height:4px;border-radius:50%;background:#c4c8cc}
.dots span.on{background:var(--blue)}

/* services */
.services{padding-top:26px;height:205px}
.service-row{display:flex;justify-content:center;gap:44px;margin-top:14px}
.service{width:90px;text-align:center}
.service svg{display:block;margin:0 auto}
.service-caption{font-size:5px;color:var(--blue);margin-top:4px}

/* testimonial */
.testimonial{background:var(--band);height:118px;text-align:center;padding-top:14px}
.quote-mark{font-size:22px;font-weight:700;color:var(--muted);line-height:1}
.testimonial p{font-size:5px;color:var(--muted);width:400px;margin:6px auto 8px}
.testimonial cite{font-style:normal;font-size:5.5px;font-weight:700;color:var(--ink)}

/* products */
.products{padding-top:20px;height:235px}
.tabs{display:flex;justify-content:center;gap:4px;margin-top:10px}
.tabs span{font-size:5px;padding:3px 6px;color:var(--ink)}
.tabs span.on{background:var(--blue);color:var(--white)}
.product-row{display:flex;justify-content:center;gap:8px;margin-top:10px}
.product{width:88px}
.product-photo{height:70px}
.product-bar{background:var(--footer);color:var(--white);padding:5px 6px;height:30px}
.product-bar b{font-size:6px;display:block}
.product-bar small{font-size:4.5px;color:#aab2ba}

/* partners */
.partners{height:110px;padding-top:8px}
.partner-row{display:flex;justify-content:center;align-items:center;gap:22px;margin-top:18px}
.partner-row .arrow{font-size:10px;color:var(--muted)}
.badge{width:38px;height:18px;background:#cfd6de;border-radius:2px}
.badge.round{width:20px;height:20px;border-radius:50%;background:#b9c8d8}

/* footer */
.site-footer{position:absolute;left:0;right:0;bottom:0;height:105px;background:var(--footer);color:#c6cbd0}
.footer-cols{display:flex;gap:28px;padding:14px 140px 0}
.footer-col{flex:1}
.footer-col h4{font-size:6px;color:var(--white);font-weight:700;margin-bottom:6px}
.footer-col li{list-style:none;font-size:4.5px;margin-bottom:3px}
.cards{display:flex;flex-wrap:wrap;gap:3px;margin-top:4px;width:50px}
.cards span{width:14px;height:9px;background:#7e8a96;border-radius:1px}
.contact-line{display:flex;gap:4px;align-items:flex-start;font-size:4.5px;margin-bottom:4px}
.contact-line svg{flex:none}
.f-field{height:9px;background:#39424b;margin-bottom:4px}
.f-send{display:inline-block;background:var(--blue);color:var(--white);font-size:4.5px;padding:2px 7px}
.footer-bottom{position:absolute;left:0;right:0;bottom:0;height:12px;background:var(--footer-deep);font-size:4.5px;padding:3px 140px;color:#8a939c}
</style>
</head>
<body>
<div class="page">

  <header class="site-header">
    <div class="top-links"><span>Login</span><span>Register</span><span class="flag"></span></div>
    <div class="brand"><span class="brand-square"></span><span class="brand-name">VELKANO</span></div>
    <nav class="main-nav">
      <a class="active" href="#">Home</a><a href="#">About</a><a href="#">Products</a><a href="#">Services</a><a href="#">Partners</a><a href="#">Contact</a>
    </nav>
  </header>

  <section class="hero">
    <div class="hero-photo" role="img" aria-label="Photo of a young plant growing from a jar of coins"></div>
    <div class="hero-copy">
      <h1 class="hero-title">BEST SERVICES YOU CAN COUNT ON!</h1>
      <p class="hero-text">We trade crude oil and precious metals worldwide and invest in property with care and trust.</p>
      <a class="btn btn-yellow" href="#">Learn More</a>
    </div>
  </section>

  <section class="about">
    <div class="about-copy">
      <h2 class="about-title">About Velkano Holdings Ltd</h2>
      <p>Velkano Holdings ltd. was founded in Cyprus in 2009 and has grown steadily ever since. Today we invest and trade across the globe, building lasting relations with partners.</p>
      <p>We specialise in buying and selling crude oil and precious metals, and in investing in selected properties. Trust guides every deal we make and every partner we serve.</p>
      <a class="btn btn-blue" href="#">Learn More</a>
    </div>
    <form class="booking">
      <h3>Book a Investment Now!</h3>
      <div class="field">Name</div>
      <div class="field">Email</div>
      <div class="field tall">Message</div>
      <span class="btn btn-yellow">Submit</span>
    </form>
  </section>

  <section class="save-banner">
    <span class="save-icon"></span>
    <div class="save-copy">
      <h3>SAVE YOUR MONEY</h3>
      <p>Get secure returns with our trusted trading plans</p>
    </div>
    <a class="btn btn-blue" href="#">Learn More</a>
  </section>

  <section class="services">
    <h2 class="section-title">Our Services</h2>
    <p class="section-intro">We offer careful trading and investment services to partners around the world, with clear terms and a team that knows each market well.</p>
    <div class="service-row">
      <div class="service">
        <svg width="80" height="86" viewBox="0 0 80 86" role="img" aria-label="Photo of banknotes and money"><polygon points="40,0 80,22 80,64 40,86 0,64 0,22" fill="#3f9a8e"/></svg>
        <div class="service-caption">Learn about oil trading</div>
      </div>
      <div class="service">
        <svg width="80" height="86" viewBox="0 0 80 86" role="img" aria-label="Photo of a modern building"><polygon points="40,0 80,22 80,64 40,86 0,64 0,22" fill="#5d86ae"/></svg>
        <div class="service-caption">Learn about metal trading</div>
      </div>
      <div class="service">
        <svg width="80" height="86" viewBox="0 0 80 86" role="img" aria-label="Photo of oil field workers"><polygon points="40,0 80,22 80,64 40,86 0,64 0,22" fill="#b98a4a"/></svg>
        <div class="service-caption">Learn about property deals</div>
      </div>
    </div>
    <div class="dots"><span class="on"></span><span></span><span></span></div>
  </section>

  <section class="testimonial">
    <div class="quote-mark">&ldquo;</div>
    <p>Working with this team has been a pleasure from day one. Their market insight, fair terms and quick answers gave us full confidence in every trade we placed together over the years.</p>
    <cite>&mdash; Daniel Reyes</cite>
    <div class="dots"><span class="on"></span><span></span><span></span></div>
  </section>

  <section class="products">
    <h2 class="section-title">Our Products</h2>
    <p class="section-intro">Our range covers crude oil, gold, silver and property shares, each chosen for steady value and sound long term growth.</p>
    <div class="tabs"><span class="on">Best Products</span><span>Popular Products</span><span>Best Selling</span><span>New Products</span></div>
    <div class="product-row">
      <div class="product"><div class="product-photo" role="img" aria-label="Photo of a city skyline" style="background:linear-gradient(#9fc1dd,#5f7e99)"></div><div class="product-bar"><b>Property</b><small>Read more</small></div></div>
      <div class="product"><div class="product-photo" role="img" aria-label="Photo of metal bars" style="background:linear-gradient(#b9bec3,#6d747b)"></div><div class="product-bar"><b>Metal</b><small>Read more</small></div></div>
      <div class="product"><div class="product-photo" role="img" aria-label="Photo of an oil pump at sunset" style="background:linear-gradient(#e2a25a,#5b3a24)"></div><div class="product-bar"><b>Crude Oil</b><small>Read more</small></div></div>
      <div class="product"><div class="product-photo" role="img" aria-label="Photo of gold coins" style="background:linear-gradient(#e8c77a,#9a6b2c)"></div><div class="product-bar"><b>Gold</b><small>Read more</small></div></div>
    </div>
    <div class="dots"><span class="on"></span><span></span><span></span></div>
  </section>

  <section class="partners">
    <h2 class="section-title">Our Partners</h2>
    <div class="partner-row">
      <span class="arrow">&lsaquo;</span>
      <span class="badge round"></span><span class="badge"></span><span class="badge"></span><span class="badge round"></span><span class="badge"></span>
      <span class="arrow">&rsaquo;</span>
    </div>
  </section>

  <footer class="site-footer">
    <div class="footer-cols">
      <div class="footer-col">
        <h4>Main Link</h4>
        <ul><li>Home</li><li>About Us</li></ul>
        <div class="cards"><span></span><span></span><span></span><span></span><span></span><span></span></div>
      </div>
      <div class="footer-col">
        <h4>Quick Link</h4>
        <ul><li>Partners</li><li>Legal Notice</li><li>Terms and conditions</li><li>Privacy policy</li><li>Contact</li></ul>
      </div>
      <div class="footer-col">
        <h4>Contact us</h4>
        <div class="contact-line"><svg width="6" height="7" viewBox="0 0 6 8"><path d="M3 0a3 3 0 0 0-3 3c0 2 3 5 3 5s3-3 3-5a3 3 0 0 0-3-3z" fill="#c6cbd0"/></svg><span>14 Harbour Lane, Larnaca, Cyprus</span></div>
        <div class="contact-line"><svg width="6" height="6" viewBox="0 0 6 6"><rect x="1.5" y="0" width="3" height="6" rx=".6" fill="#c6cbd0"/></svg><span>+357 24 555 018</span></div>
        <div class="contact-line"><svg width="7" height="5" viewBox="0 0 7 5"><rect width="7" height="5" fill="#c6cbd0"/><path d="M0 0l3.5 3L7 0" stroke="#232a31" stroke-width=".6" fill="none"/></svg><span>info@velkano-example.com</span></div>
      </div>
      <div class="footer-col">
        <h4>Quick Contact</h4>
        <div class="f-field"></div><div class="f-field"></div>
        <span class="f-send">Send</span>
      </div>
    </div>
    <div class="footer-bottom">&copy; 2024 Velkano Holdings ltd. All rights reserved.</div>
  </footer>

</div>
</body>
</html>
```